Business Card Design needed for logo design project

Our business needs a business card design. I'm not sure what format files are generally delivered back, but clearly I will need the ability to edit to add colleagues contact details.

Our logo is attached.

Brivomar is a 3D design services company, providing app, serious/educational game, VR and AR websites/applications to corporate clients.

Target Market(s)

Corporate blue-chip clients needing 3D design services

Industry/Entity Type

Business

Font styles to use
Sans Serif

Requirements
Must have
• Templated such that I can add details (name, phone number etc). Needs to include logo from previous project winner - attached.

```html
<!DOCTYPE html>
<html lang="en">
<head>
<meta charset="utf-8">
<title>Brivomar Business Card</title>
<link rel="stylesheet" href="https://fonts.googleapis.com/css2?family=PT+Sans:ital,wght@0,400;0,700;1,400&display=swap">
<style>
  :root {
    --page: #ffffff;
    --card: #ffffff;
    --card-edge: #b5b5b5;
    --brand-red: #e8202a;
    --ink: #2e2e2e;
    --ink-soft: #4a4a4a;
    --icon: #555555;
    --pattern: #efefef;
  }
  * { margin: 0; padding: 0; box-sizing: border-box; }
  html, body {
    width: 1200px; height: 849px; overflow: hidden;
    background: var(--page);
    font-family: "PT Sans", Arial, sans-serif;
  }
  .stage { position: relative; width: 1200px; height: 849px; }
  .card {
    position: absolute; top: 244px;
    width: 206px; height: 361px;
    background: var(--card);
    border: 1px solid var(--card-edge);
    box-shadow: 1px 2px 3px rgba(0,0,0,0.18);
    overflow: hidden;
  }
  .card--front { left: 343px; }
  .card--back { left: 650px; }

  .wordmark {
    position: absolute; display: flex; align-items: center; gap: 6px;
    font-weight: 400; letter-spacing: 1px;
  }
  .card--front .wordmark {
    top: 46px; left: 0; width: 100%; justify-content: center;
    font-size: 25px; color: var(--ink);
  }
  .wordmark__dot {
    width: 28px; height: 28px; border-radius: 50%;
    background: var(--brand-red); flex: none;
  }

  .person { position: absolute; left: 21px; top: 176px; }
  .person__name { font-weight: 700; font-size: 14px; color: var(--ink); line-height: 18px; }
  .person__role {
    font-style: italic; font-size: 9.5px; letter-spacing: 1.8px;
    color: var(--ink-soft); margin-top: 1px;
  }
  .accent-bar {
    position: absolute; right: 0; top: 175px;
    width: 20px; height: 37px; background: var(--brand-red);
  }

  .contacts { position: absolute; left: 51px; top: 282px; list-style: none; }
  .contacts li {
    display: flex; align-items: center; gap: 5px;
    height: 20px; font-style: italic; font-size: 10px; color: var(--ink-soft);
  }
  .contacts svg { width: 13px; height: 13px; fill: var(--icon); flex: none; }

  .icon-pattern {
    position: absolute; inset: 0; background: var(--pattern);
  }
  .brand-band {
    position: absolute; left: 0; top: 176px;
    width: 132px; height: 37px; background: var(--brand-red);
  }
  .card--back .wordmark {
    top: 0; left: 0; width: 100%; height: 100%; justify-content: center;
    gap: 5px; font-size: 15px; color: #ffffff;
  }
  .card--back .wordmark__dot { width: 16px; height: 16px; background: #ffffff; }
</style>
</head>
<body>
<main class="stage">

  <section class="card card--front" aria-label="Business card front">
    <div class="wordmark"><span class="wordmark__dot"></span>BRIVOMAR</div>

    <div class="person">
      <p class="person__name">Edmund Harrow</p>
      <p class="person__role">Founder, CEO</p>
    </div>
    <div class="accent-bar"></div>

    <ul class="contacts">
      <li>
        <svg viewBox="0 0 24 24" aria-hidden="true"><path d="M6.6 10.8c1.4 2.8 3.8 5.1 6.6 6.6l2.2-2.2c.3-.3.7-.4 1-.2 1.1.4 2.3.6 3.6.6.6 0 1 .4 1 1V20c0 .6-.4 1-1 1C10.6 21 3 13.4 3 4c0-.6.4-1 1-1h3.5c.6 0 1 .4 1 1 0 1.3.2 2.5.6 3.6.1.3 0 .7-.2 1l-2.3 2.2z"/></svg>
        0090 541 220 6718
      </li>
      <li>
        <svg viewBox="0 0 24 24" aria-hidden="true"><path d="M2 5h20v14H2z M3.5 6.5v.4L12 13l8.5-6.1v-.4z" fill-rule="evenodd"/></svg>
        info@brivomar.com
      </li>
      <li>
        <svg viewBox="0 0 24 24" aria-hidden="true"><path d="M12 2C8.1 2 5 5.1 5 9c0 5.2 7 13 7 13s7-7.8 7-13c0-3.9-3.1-7-7-7zm0 9.5a2.5 2.5 0 1 1 0-5 2.5 2.5 0 0 1 0 5z"/></svg>
        14C, Linden Row
      </li>
    </ul>
  </section>

  <section class="card card--back" aria-label="Business card back">
    <div class="icon-pattern" role="img" aria-label="Pattern of grey outline technology icons: laptops, monitors, phones, tablets, graduation caps, chat bubbles, camera, cloud, padlocks, heart and smiley"></div>
    <div class="brand-band">
      <div class="wordmark"><span class="wordmark__dot"></span>BRIVOMAR</div>
    </div>
  </section>

</main>
</body>
</html>
```